Township of Quenford E-Alert Signup

Need to create print media that is designed for a Town in New Jersey that is starting a marketing campaign to get townspeople to sign up for the E-Alert system.Need print media that is 1. interchangeable in size (regular letter-size, as well as a poster size) 2. Branded with their colors, logo, etc. (green and white displayed in logo)3. Displays the incentives to sign up. Incentives:- Community Services/Announcements- Gov’t/Non-profit Resources- Tax Information- Employment opportunities- Municipal Services/Public Works/Recreation Divisions- Health Updates
Target Market(s)
Townspeople of Maplewood NJ
Industry/Entity Type
Government
Colors
Designer to choose colors to be used in the design.
Requirements
Must have
- 1. interchangeable in size (regular letter-size, as well as a poster size)
- 2. Branded with their colors, logo, etc. (green and white displayed in logo)
- 3. Displays the incentives to sign up.
- Incentives:
- - Community Services/Announcements
- - Gov’t/Non-profit Resources
- - Tax Information
- - Employment opportunities
- - Municipal Services/Public Works/Recreation Divisions
- - Health Updates

```html
<!DOCTYPE html>
<html lang="en">
<head>
<meta charset="UTF-8">
<title>Township of Quenford E-Alert Signup</title>
<link href="https://fonts.googleapis.com/css2?family=Open+Sans:wght@400;600;700&family=Oswald:wght@500&family=Tinos:wght@400;700&display=swap" rel="stylesheet">
<style>
  :root {
    --green-dark: #1c4a24;
    --green: #1f6a2f;
    --green-mid: #2f8a3c;
    --green-light: #7fb069;
    --cream: #f6f2e2;
    --cream-deep: #e9e3c8;
    --ink: #1e1e1e;
    --white: #ffffff;
  }
  * { margin: 0; padding: 0; box-sizing: border-box; }
  html, body { width: 1012px; height: 1200px; overflow: hidden; background: #eeeeee; }
  .flyer {
    position: relative; width: 1012px; height: 1200px; overflow: hidden;
    background: linear-gradient(180deg, var(--cream) 40%, var(--cream-deep) 100%);
    font-family: "Open Sans", Arial, sans-serif; color: var(--ink);
  }
  .hero-photo {
    position: absolute; left: 0; top: 0; width: 1012px; height: 520px;
    background: linear-gradient(180deg, #4d6fb5 0%, #8aa3cf 30%, #9b8f7c 55%, #6a5a4a 75%, #4a4844 100%);
  }
  .hero-wave { position: absolute; left: 0; top: 0; width: 1012px; height: 560px; }
  .seal {
    position: absolute; left: 93px; top: 285px; width: 250px; height: 250px;
    border-radius: 50%; background: var(--white);
    display: flex; align-items: center; justify-content: center; text-align: center;
  }
  .seal-name {
    color: var(--green); font-family: "Tinos", "Times New Roman", serif; font-weight: 700;
    font-size: 30px; line-height: 1.15; padding: 0 30px;
  }
  .headline-lead {
    position: absolute; left: 88px; top: 584px;
    font-family: "Tinos", "Times New Roman", serif; font-size: 36px; color: var(--ink);
  }
  .headline-banner {
    position: absolute; left: 0; top: 632px; width: 520px; height: 68px;
  }
  .headline-main {
    position: absolute; left: 45px; top: 632px; height: 68px; line-height: 68px;
    font-family: "Tinos", "Times New Roman", serif; font-weight: 700; font-size: 54px; color: var(--white);
  }
  .incentives-title {
    position: absolute; left: 45px; top: 740px;
    font-weight: 700; font-size: 28px; color: var(--green);
  }
  .incentive-list { position: absolute; left: 45px; top: 786px; list-style: none; }
  .incentive-list li {
    display: flex; align-items: center; gap: 16px;
    height: 44.3px; font-size: 24px;
  }
  .tick { width: 26px; height: 26px; flex: none; }
  .monitor { position: absolute; left: 560px; top: 598px; width: 385px; height: 300px; }
  .monitor-screen {
    position: absolute; left: 584px; top: 620px; width: 337px; height: 190px;
    background: linear-gradient(135deg, #5e6f4a 0%, #3f4a3c 45%, #6f7a6a 60%, #3e5a32 100%);
  }
  .badge { position: absolute; left: 760px; top: 788px; width: 206px; height: 206px; }
  .badge-text {
    position: absolute; left: 760px; top: 836px; width: 206px; text-align: center;
    font-family: "Oswald", Impact, sans-serif; font-weight: 500; font-size: 34px; line-height: 1.2;
    color: var(--white); text-transform: uppercase;
  }
  .footer {
    position: absolute; left: 0; top: 1118px; width: 1012px; height: 82px; background: var(--green-dark);
  }
  .footer-address {
    position: absolute; left: 0; top: 1160px; width: 1012px; text-align: center;
    font-size: 20px; color: var(--white);
  }
  .web-pill {
    position: absolute; left: 285px; top: 1094px; width: 442px; height: 54px;
    border-radius: 27px; background: var(--green);
    display: flex; align-items: center; justify-content: center; gap: 10px;
    color: var(--white); font-weight: 700; font-size: 24px;
  }
  .globe { width: 26px; height: 26px; }
</style>
</head>
<body>
<main class="flyer">
  <div class="hero-photo" role="img" aria-label="Photo of a downtown street corner with Tudor-style brick shops, awnings and outdoor café umbrellas under a blue sky"></div>

  <svg class="hero-wave" viewBox="0 0 1012 560" aria-hidden="true">
    <path d="M0,452 C260,390 560,520 1012,478 L1012,560 L0,560 Z" fill="var(--green-mid)"/>
    <path d="M0,468 C260,408 560,538 1012,496 L1012,560 L0,560 Z" fill="var(--green)"/>
    <path d="M0,488 C260,440 560,560 1012,520 L1012,560 L0,560 Z" fill="var(--cream)"/>
  </svg>

  <div class="seal"><span class="seal-name">Township of Quenford</span></div>

  <p class="headline-lead">SIGN UP FOR A</p>
  <svg class="headline-banner" viewBox="0 0 520 68" aria-hidden="true">
    <polygon points="0,0 505,0 520,68 0,68" fill="var(--green)"/>
  </svg>
  <h1 class="headline-main">E-Alert system</h1>

  <h2 class="incentives-title">INCENTIVES:</h2>
  <ul class="incentive-list">
    <li><svg class="tick" viewBox="0 0 26 26"><rect x="2" y="5" width="18" height="18" rx="2" fill="none" stroke="var(--green)" stroke-width="2.5"/><path d="M6,13 L11,18 L24,3" fill="none" stroke="var(--green)" stroke-width="3"/></svg>Community Services/Announcements</li>
    <li><svg class="tick" viewBox="0 0 26 26"><rect x="2" y="5" width="18" height="18" rx="2" fill="none" stroke="var(--green)" stroke-width="2.5"/><path d="M6,13 L11,18 L24,3" fill="none" stroke="var(--green)" stroke-width="3"/></svg>Gov’t/Non-profit Resources</li>
    <li><svg class="tick" viewBox="0 0 26 26"><rect x="2" y="5" width="18" height="18" rx="2" fill="none" stroke="var(--green)" stroke-width="2.5"/><path d="M6,13 L11,18 L24,3" fill="none" stroke="var(--green)" stroke-width="3"/></svg>Tax Information</li>
    <li><svg class="tick" viewBox="0 0 26 26"><rect x="2" y="5" width="18" height="18" rx="2" fill="none" stroke="var(--green)" stroke-width="2.5"/><path d="M6,13 L11,18 L24,3" fill="none" stroke="var(--green)" stroke-width="3"/></svg>Employment opportunities</li>
    <li><svg class="tick" viewBox="0 0 26 26"><rect x="2" y="5" width="18" height="18" rx="2" fill="none" stroke="var(--green)" stroke-width="2.5"/><path d="M6,13 L11,18 L24,3" fill="none" stroke="var(--green)" stroke-width="3"/></svg>Municipal Services/Public Works/Recreation Divisions</li>
    <li><svg class="tick" viewBox="0 0 26 26"><rect x="2" y="5" width="18" height="18" rx="2" fill="none" stroke="var(--green)" stroke-width="2.5"/><path d="M6,13 L11,18 L24,3" fill="none" stroke="var(--green)" stroke-width="3"/></svg>Health Updates</li>
  </ul>

  <svg class="monitor" viewBox="0 0 385 300" aria-hidden="true">
    <rect x="0" y="0" width="385" height="250" rx="10" fill="#1b1b1b"/>
    <rect x="0" y="222" width="385" height="28" fill="#d9d9d9"/>
    <path d="M160,250 L225,250 L232,290 L153,290 Z" fill="#bdbdbd"/>
    <ellipse cx="192" cy="292" rx="62" ry="6" fill="#a8a8a8"/>
  </svg>
  <div class="monitor-screen" role="img" aria-label="Aerial photo of a street intersection with a rainbow-painted crosswalk"></div>

  <svg class="badge" viewBox="0 0 206 206" aria-hidden="true">
    <polygon fill="var(--green)" points="103,0 116,14 133,5 141,22 160,19 163,38 182,41 180,60 198,68 190,85 204,98 192,113 201,131 184,139 187,158 168,161 165,180 146,178 138,196 121,188 108,204 93,191 76,202 67,185 48,189 44,170 25,168 26,149 8,140 16,123 2,110 14,95 4,78 21,70 18,51 37,47 40,28 59,29 67,11 84,19 "/>
  </svg>
  <p class="badge-text">Signup for<br>E-Alerts</p>

  <div class="footer"></div>
  <div class="web-pill">
    <svg class="globe" viewBox="0 0 26 26"><circle cx="13" cy="13" r="11" fill="none" stroke="var(--white)" stroke-width="2.5"/><path d="M2,13 H24 M13,2 C7,8 7,18 13,24 M13,2 C19,8 19,18 13,24" fill="none" stroke="var(--white)" stroke-width="2"/></svg>
    www.twp.quenford.nj.us
  </div>
  <p class="footer-address">218 Alder St., Quenford Township, NJ 07099 &nbsp;|&nbsp; Ph: (973) 555-0142</p>
</main>
</body>
</html>
```